Emergency Dental Referral Company

I need a brochure to advertise my business to prospective dentists that may want to join or to dentists that may want to use this for their own patients. I also need to advertise this brochure to ER physicians who see many dental emergencies. This brochure is meant to be dual purpose: advertise our company and services to the ER physicians who then hand out the brochures to the dental emergency patients in pain. See our website for further details at www.fernvalepath.example

I will also be attaching our logo design.

Target Market(s)

Emergency Room physicians and other medical personnel who will distribute these brochures to patients in dental pain and dental emergencies

Industry/Entity Type

Business

Font styles to use
Serif
Sans Serif

Requirements
Must have
• Must be simple! Must have a call to action- inspiration to go to website. Highlight our guarantee that states "If you are not seen by a dentist in 24 hours or less, you will receive your money back. Emphasis on the logo. Must discuss how we find a dentist in your zip code in three easy steps.
• For the color- please make similar to our website of www.fernvalepath.example
Nice to have
• Would like to state that this service can see patients at any hour of the day.
Should not have
• no contact information besides the URL. www.fernvalepath.example

```html
<!DOCTYPE html>
<html lang="en">
<head>
<meta charset="utf-8">
<title>Find a Dentist in 3 Easy Steps – Fernvale Path</title>
<link rel="stylesheet" href="https://fonts.googleapis.com/css2?family=Oswald:wght@500;600&family=Open+Sans:wght@400;700&display=swap">
<style>
  :root {
    --brand-blue: #1f6fb5;
    --ink: #1a1a1a;
    --band-green: #9dc23a;
    --white: #ffffff;
    --rule: #3a3a3a;
    --photo-light: #f4f7fa;
    --photo-mid: #d9e3ec;
    --photo-deep: #b9c8d6;
  }
  * { margin: 0; padding: 0; box-sizing: border-box; }
  html, body { width: 1200px; height: 800px; overflow: hidden; background: var(--white); }
  .flyer {
    position: relative;
    width: 1200px;
    height: 800px;
    overflow: hidden;
    font-family: "Open Sans", sans-serif;
    color: var(--ink);
  }
  .flyer__photo {
    position: absolute;
    inset: 0;
    background:
      linear-gradient(90deg, rgba(255,255,255,0.95) 0%, rgba(255,255,255,0.75) 28%, rgba(255,255,255,0) 50%),
      radial-gradient(ellipse at 68% 70%, #c9a79a 0%, rgba(201,167,154,0) 38%),
      linear-gradient(120deg, var(--photo-light) 0%, var(--photo-mid) 55%, var(--photo-deep) 100%);
  }
  .headline {
    position: absolute;
    left: 66px;
    top: 70px;
    font-family: "Oswald", sans-serif;
    font-weight: 500;
    color: var(--brand-blue);
    text-transform: uppercase;
    line-height: 1;
  }
  .headline__lead { display: block; font-size: 44px; letter-spacing: 0.5px; }
  .headline__main { display: block; font-size: 92px; font-weight: 600; margin-top: 6px; letter-spacing: 1px; }
  .steps {
    position: absolute;
    left: 80px;
    top: 250px;
    height: 440px;
    border-left: 2px solid var(--rule);
    list-style: none;
  }
  .step { position: relative; padding-left: 32px; margin-bottom: 44px; }
  .step::before {
    content: "";
    position: absolute;
    left: -8px;
    top: 14px;
    width: 10px;
    height: 10px;
    border: 2px solid var(--rule);
    border-radius: 50%;
    background: var(--white);
  }
  .step__number { font-size: 28px; font-weight: 700; text-transform: uppercase; line-height: 1.15; }
  .step__title { font-size: 19px; font-weight: 700; line-height: 1.3; }
  .step__text { font-size: 17px; line-height: 1.4; max-width: 330px; }
  .brand {
    position: absolute;
    right: 110px;
    top: 70px;
    display: flex;
    align-items: center;
    gap: 12px;
    font-family: "Open Sans", sans-serif;
    font-weight: 700;
    font-size: 34px;
    color: var(--brand-blue);
  }
  .brand__dot { width: 22px; height: 22px; border-radius: 50%; background: var(--brand-blue); }
  .guarantee-band {
    position: absolute;
    left: 0;
    bottom: 0;
    width: 100%;
    height: 112px;
    background: var(--band-green);
    display: flex;
    align-items: center;
    justify-content: space-between;
    padding: 0 50px 0 66px;
    color: var(--white);
  }
  .guarantee { font-size: 23px; line-height: 1.3; }
  .guarantee strong { font-weight: 700; }
  .site-url {
    font-family: "Oswald", sans-serif;
    font-weight: 500;
    font-size: 44px;
    text-transform: uppercase;
    letter-spacing: 0.5px;
  }
</style>
</head>
<body>
  <main class="flyer">
    <div class="flyer__photo" role="img" aria-label="Photo of a dentist examining a young woman patient in a dental chair"></div>

    <h1 class="headline">
      <span class="headline__lead">Find a dentist in</span>
      <span class="headline__main">3 easy steps</span>
    </h1>

    <ol class="steps">
      <li class="step">
        <p class="step__number">Step 1</p>
        <p class="step__title">Fill out a Form</p>
        <p class="step__text">We will need your Zip code and contact information.</p>
      </li>
      <li class="step">
        <p class="step__number">Step 2</p>
        <p class="step__title">Find a Dentist</p>
        <p class="step__text">Opportunity to choose among the most profitable and the most qualified dentist in your area.</p>
      </li>
      <li class="step">
        <p class="step__number">Step 3</p>
        <p class="step__title">Get your appointment</p>
        <p class="step__text">Get your emergency appointment</p>
      </li>
    </ol>

    <div class="brand">
      <span class="brand__dot"></span>
      <span class="brand__name">Fernvale Path</span>
    </div>

    <footer class="guarantee-band">
      <p class="guarantee">If you are not seen by a dentist in 24 hours or less,<br><strong>you will receive your money back.</strong></p>
      <p class="site-url">www.fernvalepath.example</p>
    </footer>
  </main>
</body>
</html>
```